Child sleep consultant needs a flyer to attract new clients

We need a flyer that will attract the attention of parents with children between newborn and 3 years old who may be experiencing sleep issues. The flyer will be placed at places such as community centres, doctors room, play centres, etc.

Our business is called Hushwood Nestlings and provides a sleep consultancy service. Our service essentially provides a routine for parents to follow and general advice. Our service is not medical advice.

We need the flyer to have an overall tone that is soft and peaceful however can catch the attention of parents who may be struggling on minimal sleep. We would like photos with minimal text. The colour we use is green.

We will provide the text to appear in the flyer once we have a better idea of the layout that we prefer for the flyer. The text however wont be extensive, just some catchy points.

We want to direct people to our website which is hushwoodnestlings.com.au. We also have a facebook page, which is Hushwood Nestlings.

We have a logo that we would like to appear on the flyer. We will attach the file once the uploader on pixel bazaar is fixed.

Our consultant is a certified Dream Anchor consultant, which has a separate logo that should appear somewhere on the logo. I will attach this once the uploader is fixed.

When we print the flyer - we want to print A5 SIZE ... please make sure the formatting is OK for this size.

Target Market(s)

Mums and Dads with children between newborn and 3 years old.

Industry/Entity Type

Consultant

Colors
cadf82

Requirements
Must have
• - Our logo.
• - Dream Anchor consultant logo - both attached to this brief.
• - Contact details - including phone number, email address and website
• - MUST be suitable for A5 printable size, double sided please.
• Must have the following text:
• If your baby or toddler isn't sleeping through the night, neither are you - and this means you are probably feeling physically and mentally exhausted, stressed, depressed and irritable, afraid you might be damaging your child and disconnected from your partner.
• The good news is nearly all healthy children 3 months or older are physically capable of sleeping 12 solid hours without waking. They just need to be taught the healthy sleep habits that enable them to do so.
• I can help with the sleep issues your child is experiencing. As a certified Dream Anchor (insert trademark TM here) I can help if:
• - your child will only fall asleep when nursing or bottle feeding
• - your child needs a dummy in order fall asleep
• - you're waking up with your child one or more times per night
• - your child needs to be rocked, patted, or taken for a car ride to go to sleep
• - your own lack of sleep is starting to take a toll on your family
• I've been personally trained by Marla Penwick, best selling author of the Dream Anchor (insert trade mark symbol here) Program to teach her sleep training methods to families like yours. Marla's methods have already helped over 30,000 parents and children and I'd be delighted to help your family next!
• Call or email for a free 15 minute consultation
• I would love to connect with you to talk about your child's specific situation and discuss different solutions.

```html
<!DOCTYPE html>
<html lang="en">
<head>
<meta charset="utf-8">
<title>Hushwood Nestlings – Flyer Front and Back</title>
<link rel="stylesheet" href="https://fonts.googleapis.com/css2?family=Roboto:wght@300;400;700&family=Roboto+Slab:wght@300;400&family=Tinos&display=swap">
<style>
  :root {
    --leaf: #acd04b;
    --leaf-pale: #cfe49a;
    --moss: #58703f;
    --ink: #454545;
    --body-ink: #333333;
    --paper: #ffffff;
    --shadow: #d4d4d6;
    --photo-light: #f6f1ee;
    --photo-warm: #e9cfc6;
  }
  * { margin: 0; padding: 0; box-sizing: border-box; }
  html, body { width: 1200px; height: 889px; overflow: hidden; background: var(--paper); }
  body { position: relative; font-family: "Roboto", Arial, sans-serif; color: var(--ink); }

  .side-label {
    position: absolute; top: 22px; font-size: 32px; font-weight: 400; color: #222;
    transform: translateX(-50%);
  }
  .side-label--front { left: 215px; }
  .side-label--back { left: 898px; }

  /* ---------- Front ---------- */
  .flyer-front {
    position: absolute; left: 0; top: 77px; width: 540px; height: 802px;
    overflow: hidden; background: var(--paper); border: 1px solid #e3ecc8;
  }
  .flyer-front__shapes { position: absolute; inset: 0; }
  .front-title {
    position: absolute; left: 20px; top: 22px; font-family: "Tinos", "Times New Roman", serif;
    font-size: 37px; font-weight: 400; color: var(--paper); letter-spacing: 0.3px; white-space: nowrap;
  }
  .offer-badge {
    position: absolute; left: 422px; top: 426px; font-size: 58px; font-weight: 700; color: var(--paper);
  }
  .front-questions {
    position: absolute; left: 22px; top: 500px; font-family: "Roboto Slab", Georgia, serif;
    font-weight: 300; font-size: 26px; line-height: 36px; color: var(--leaf);
  }
  .brand-mark {
    position: absolute; left: 22px; top: 672px; display: flex; align-items: center; gap: 8px;
  }
  .brand-mark__dot { width: 34px; height: 34px; border-radius: 50%; background: var(--leaf); }
  .brand-mark__name { font-size: 17px; line-height: 20px; font-weight: 400; color: var(--leaf); width: 90px; }
  .helping-hand {
    position: absolute; left: 166px; top: 644px; font-size: 25px; font-weight: 300; color: var(--leaf);
  }
  .helping-copy {
    position: absolute; left: 164px; top: 678px; width: 340px; font-size: 8.3px; line-height: 10.6px; color: var(--body-ink);
  }
  .helping-copy p + p { margin-top: 2px; }
  .front-footer {
    position: absolute; left: 0; bottom: 0; width: 100%; height: 46px; background: var(--leaf);
    color: var(--paper); font-size: 27px; text-align: center; line-height: 46px;
  }

  /* ---------- Back ---------- */
  .flyer-back {
    position: absolute; left: 615px; top: 55px; width: 585px; height: 834px; overflow: hidden;
  }
  .flyer-back__shapes { position: absolute; inset: 0; }
  .icon-label {
    position: absolute; font-size: 12.5px; color: var(--body-ink); white-space: nowrap; transform: translateX(-50%);
  }
  .icon-label--email { left: 161px; top: 90px; }
  .icon-label--contact { left: 355px; top: 102px; }
  .icon-label--web { left: 335px; top: 763px; transform: none; }
  .back-heading {
    position: absolute; font-size: 26px; font-weight: 400; letter-spacing: 0.3px; white-space: nowrap;
  }
  .back-heading--upper { left: 261px; top: 300px; transform: translateX(-50%); color: var(--ink); }
  .back-heading--lower { left: 21px; top: 626px; color: var(--moss); }
  .back-copy--upper {
    position: absolute; left: 53px; top: 335px; width: 395px; font-size: 9.6px; line-height: 13.4px; color: var(--paper);
  }
  .back-copy--upper p + p { margin-top: 3px; }
  .back-statement {
    position: absolute; left: 88px; top: 456px; font-size: 19px; line-height: 23px; color: var(--paper); font-weight: 400;
  }
  .headline {
    position: absolute; left: 302px; top: 505px; font-size: 84px; font-weight: 300; line-height: 82px;
    color: var(--paper); letter-spacing: 2px;
  }
  .back-copy--lower {
    position: absolute; left: 21px; top: 662px; width: 228px; font-size: 9.5px; line-height: 12.5px; color: var(--body-ink);
  }
  .help-list { list-style: none; margin-top: 2px; }
  .help-list li { position: relative; padding-left: 9px; }
  .help-list li::before { content: "–"; position: absolute; left: 0; color: var(--moss); }
</style>
</head>
<body>

<div class="side-label side-label--front">Front</div>
<div class="side-label side-label--back">Back</div>

<section class="flyer-front">
  <svg class="flyer-front__shapes" width="540" height="802" viewBox="0 0 540 802">
    <defs>
      <radialGradient id="babyTones" cx="45%" cy="45%" r="65%">
        <stop offset="0%" stop-color="var(--photo-warm)"/>
        <stop offset="60%" stop-color="var(--photo-light)"/>
        <stop offset="100%" stop-color="#e8e6e8"/>
      </radialGradient>
      <clipPath id="belowHeader"><rect x="0" y="84" width="540" height="720"/></clipPath>
    </defs>
    <rect x="0" y="0" width="540" height="84" fill="var(--leaf)"/>
    <g clip-path="url(#belowHeader)">
      <circle cx="191" cy="230" r="276" fill="none" stroke="var(--leaf)" stroke-width="3"/>
      <circle cx="191" cy="230" r="271" fill="url(#babyTones)" role="img" aria-label="Photo of a sleeping baby"/>
    </g>
    <circle cx="540" cy="464" r="138" fill="var(--leaf)"/>
    <rect x="0" y="756" width="540" height="46" fill="var(--leaf)"/>
  </svg>

  <h1 class="front-title">ARE YOU EXHAUSTED??</h1>
  <div class="offer-badge">+10</div>
  <p class="front-questions">Having Difficulties<br>To Put Your Child To Sleep?<br>Feeling Stress When Working?</p>

  <div class="brand-mark">
    <span class="brand-mark__dot"></span>
    <span class="brand-mark__name">Hushwood Nestlings</span>
  </div>
  <h2 class="helping-hand">Need a helping hand?</h2>
  <div class="helping-copy">
    <p>If your baby or toddler isn't sleeping through the night, neither are you - and this means you are probably feeling physically and mentally exhausted, stressed, depressed and irritable, afraid you might be damaging your child and disconnected from your partner.</p>
    <p>I would love to connect with you to talk about your child's specific situation and discuss different solutions.</p>
  </div>

  <footer class="front-footer">hushwoodnestlings.com.au</footer>
</section>

<section class="flyer-back">
  <svg class="flyer-back__shapes" width="585" height="834" viewBox="0 0 585 834">
    <defs>
      <clipPath id="mainCircle"><circle cx="262" cy="432" r="238"/></clipPath>
    </defs>
    <circle cx="262" cy="432" r="238" fill="var(--leaf)"/>
    <circle cx="365" cy="581" r="138" fill="var(--leaf-pale)"/>
    <circle cx="365" cy="581" r="138" fill="var(--moss)" clip-path="url(#mainCircle)"/>

    <circle cx="80" cy="218" r="86" fill="var(--shadow)"/>
    <circle cx="87" cy="215" r="83" fill="#efefef" stroke="var(--paper)" stroke-width="6" role="img" aria-label="Round photo of a family moment"/>
    <circle cx="249" cy="148" r="83" fill="var(--shadow)"/>
    <circle cx="256" cy="145" r="80" fill="#efefef" stroke="var(--paper)" stroke-width="6" role="img" aria-label="Round photo of a calm nursery"/>

    <g class="icon icon--email">
      <circle cx="161" cy="150" r="38" fill="var(--moss)"/>
      <rect x="141" y="136" width="40" height="28" rx="2" fill="var(--paper)"/>
      <path d="M141 137 L161 153 L181 137" fill="none" stroke="var(--moss)" stroke-width="2.5"/>
    </g>
    <g class="icon icon--contact">
      <circle cx="355" cy="162" r="38" fill="var(--moss)"/>
      <circle cx="355" cy="151" r="11" fill="var(--paper)"/>
      <path d="M334 180 Q336 164 355 164 Q374 164 376 180 Z" fill="var(--paper)"/>
    </g>
    <g class="icon icon--home">
      <circle cx="287" cy="770" r="37" fill="var(--moss)"/>
      <path d="M266 772 L287 752 L308 772" fill="none" stroke="var(--paper)" stroke-width="4" stroke-linejoin="round"/>
      <path d="M272 770 L272 789 L283 789 L283 778 L291 778 L291 789 L302 789 L302 770 L287 756 Z" fill="var(--paper)"/>
    </g>
  </svg>

  <span class="icon-label icon-label--email">hello@hushwoodnestlings.com.au</span>
  <span class="icon-label icon-label--contact">0400 512 738</span>
  <span class="icon-label icon-label--web">hushwoodnestlings.com.au</span>

  <h2 class="back-heading back-heading--upper">THE GOOD NEWS</h2>
  <div class="back-copy--upper">
    <p>The good news is nearly all healthy children 3 months or older are physically capable of sleeping 12 solid hours without waking. They just need to be taught the healthy sleep habits that enable them to do so.</p>
    <p>I've been personally trained by Marla Penwick, best selling author of the Dream Anchor™ Program to teach her sleep training methods to families like yours. Marla's methods have already helped over 30,000 parents and children and I'd be delighted to help your family next!</p>
  </div>
  <p class="back-statement">CALL OR EMAIL<br>FOR A FREE<br>15 MINUTE<br>CONSULTATION</p>
  <div class="headline">REST<br>EASY</div>

  <h2 class="back-heading back-heading--lower">I CAN HELP IF</h2>
  <div class="back-copy--lower">
    <p>I can help with the sleep issues your child is experiencing. As a certified Dream Anchor™ I can help if:</p>
    <ul class="help-list">
      <li>your child will only fall asleep when nursing or bottle feeding</li>
      <li>your child needs a dummy in order fall asleep</li>
      <li>you're waking up with your child one or more times per night</li>
      <li>your child needs to be rocked, patted, or taken for a car ride to go to sleep</li>
      <li>your own lack of sleep is starting to take a toll on your family</li>
    </ul>
  </div>
</section>

</body>
</html>
```